Presentation folder for holding wedding cake literature

We need to have a front cover design as well as a back cover design for a presentation folder to hold literature for a bakery who sells a lot of wedding cakes.

We have uploaded a couple copies of ideas that we like. They are for demonstrative purposes only.

The text on the front cover needs to be:
-The Sugar Atelier-
-Designing, baking and decorating perfect wedding cakes...Guaranteed!

On the back cover it needs to say:
-Serving VELVAsoft cakes and a "Silver Ribbon" Experience-

In addition the back cover must contain the "Silver Ribbon Baker" logo.

We will only supply photos if necessary. We would rather have you choose them.

We are open to any colors as long as they are soft.

For a reference of the client, go to http://www.brindlefieldsugaratelier.example

Target Market(s)

The target market is primarily women ages 25-40.

Industry/Entity Type

Wedding

Requirements
Must have
• Must have priorities are listed in the brief.
Nice to have
• Fonts should be a combination of "script" and one or more complementary styles.

Colors should be either a soft blue, pinkish tone or lavender tone. Mixing any of the colors with a light gray would be acceptable as well.
Should not have
• No dark colors such as black, red, purple, green or orange.

```html
<!DOCTYPE html>
<html lang="en">
<head>
<meta charset="utf-8">
<title>The Sugar Atelier – Presentation Folder</title>
<link rel="stylesheet" href="https://fonts.googleapis.com/css2?family=Cinzel:wght@400;600&family=Dancing+Script:wght@700&display=swap">
<style>
  :root {
    --canvas: #f4f6f8;
    --paper: #fbfdfe;
    --paper-tint: #eef6fb;
    --sky: #4fb8e6;
    --sky-deep: #3aa6d8;
    --lace: #bfe2f3;
    --frost: #d8edf7;
    --gold: #c9992d;
    --white: #ffffff;
  }
  * { margin: 0; padding: 0; box-sizing: border-box; }
  html, body { width: 1200px; height: 847px; overflow: hidden; background: var(--canvas); }
  .folder-spread {
    position: relative; width: 1200px; height: 847px;
  }
  .cover {
    position: absolute; top: 53px; width: 540px; height: 740px;
    background: radial-gradient(ellipse at 50% 40%, var(--paper) 0%, var(--paper-tint) 100%);
    box-shadow: 0 2px 10px rgba(60, 90, 110, 0.12);
    overflow: hidden;
  }
  .cover--back { left: 60px; }
  .cover--front { left: 600px; }

  .lace-band { position: absolute; left: 0; width: 100%; height: 12px; background: var(--lace); }
  .ribbon-band { position: absolute; left: 0; width: 100%; background: var(--sky); }

  /* Front cover */
  .front-header .lace-band--top { top: 40px; }
  .front-header .ribbon-band { top: 52px; height: 48px; }
  .front-header .lace-band--under { top: 100px; }
  .brand-title {
    position: absolute; top: 54px; right: 34px;
    font-family: "Dancing Script", cursive; font-weight: 700;
    font-size: 36px; line-height: 44px; color: var(--white);
  }
  .brand-tagline {
    position: absolute; top: 118px; left: 0; width: 100%; text-align: center;
    font-family: "Cinzel", serif; font-size: 11px; letter-spacing: 0.6px;
    color: var(--sky-deep);
  }
  .photo-collage { position: absolute; left: 0; top: 0; width: 100%; height: 100%; }
  .photo {
    position: absolute; border: 4px solid var(--white);
    box-shadow: 0 1px 4px rgba(0,0,0,0.18);
  }
  .photo--tiered-cake { left: 160px; top: 235px; width: 150px; height: 120px; background: linear-gradient(160deg, #e6e3e6, #a9a7b0); }
  .photo--garden-cake { left: 305px; top: 220px; width: 130px; height: 150px; background: linear-gradient(170deg, #8fb08a, #e8e6e0); transform: rotate(12deg); }
  .photo--first-kiss { left: 95px; top: 340px; width: 90px; height: 80px; background: linear-gradient(150deg, #d9c9c2, #6e5a56); }
  .photo--cake-cutting { left: 178px; top: 385px; width: 170px; height: 120px; background: linear-gradient(140deg, #f1ece8, #4a5d8a); transform: rotate(-4deg); }
  .photo--ribbon-cake { left: 330px; top: 360px; width: 145px; height: 90px; background: linear-gradient(160deg, #5b4a3a, #e9e2d8); transform: rotate(-2deg); }

  .band-group .lace-band--top { top: 612px; }
  .band-group .ribbon-band { top: 624px; height: 38px; }
  .band-group .lace-band--under { top: 662px; }

  /* Back cover */
  .promise-frame {
    position: absolute; left: 80px; top: 105px; width: 270px; height: 140px;
  }
  .promise-frame__ornament {
    position: absolute; inset: 0; border-radius: 14px;
    background: var(--frost); opacity: 0.7;
  }
  .promise-text {
    position: absolute; inset: 0; display: flex; flex-direction: column;
    justify-content: center; align-items: center; text-align: center;
    font-family: "Cinzel", serif; font-weight: 600; font-size: 13px;
    line-height: 19px; color: var(--gold); letter-spacing: 0.4px;
  }
  .baker-mark {
    position: absolute; left: 90px; top: 440px; display: flex; align-items: center; gap: 14px;
  }
  .baker-mark__dot { width: 34px; height: 34px; border-radius: 50%; background: var(--sky); }
  .baker-mark__name {
    font-family: "Cinzel", serif; font-weight: 600; font-size: 30px;
    color: var(--gold); line-height: 1;
  }
</style>
</head>
<body>
<main class="folder-spread">

  <section class="cover cover--back" aria-label="Back cover">
    <div class="promise-frame">
      <div class="promise-frame__ornament" role="img" aria-label="Ornate scrollwork frame in sky blue"></div>
      <p class="promise-text">
        <span>Serving VELVAsoft cakes</span>
        <span>and</span>
        <span>a "Silver Ribbon" Experience</span>
      </p>
    </div>

    <div class="baker-mark">
      <span class="baker-mark__dot"></span>
      <span class="baker-mark__name">Silver Ribbon Baker</span>
    </div>

    <div class="band-group">
      <div class="lace-band lace-band--top" role="img" aria-label="Blue lace border"></div>
      <div class="ribbon-band"></div>
      <div class="lace-band lace-band--under" role="img" aria-label="Blue lace border"></div>
    </div>
  </section>

  <section class="cover cover--front" aria-label="Front cover">
    <header class="front-header">
      <div class="lace-band lace-band--top" role="img" aria-label="Blue lace border"></div>
      <div class="ribbon-band"></div>
      <div class="lace-band lace-band--under" role="img" aria-label="Blue lace border"></div>
      <h1 class="brand-title">The Sugar Atelier</h1>
      <p class="brand-tagline">Designing, baking and decorating perfect wedding cakes . . . Guaranteed!</p>
    </header>

    <div class="photo-collage">
      <div class="photo photo--garden-cake" role="img" aria-label="Photo of a five-tier white wedding cake outdoors"></div>
      <div class="photo photo--tiered-cake" role="img" aria-label="Photo of a white tiered cake with sugar roses and champagne glasses"></div>
      <div class="photo photo--first-kiss" role="img" aria-label="Photo of a couple at their reception"></div>
      <div class="photo photo--ribbon-cake" role="img" aria-label="Photo of a tiered cake with blue ribbons"></div>
      <div class="photo photo--cake-cutting" role="img" aria-label="Photo of a bride and groom cutting their wedding cake"></div>
    </div>

    <div class="band-group">
      <div class="lace-band lace-band--top" role="img" aria-label="Blue lace border"></div>
      <div class="ribbon-band"></div>
      <div class="lace-band lace-band--under" role="img" aria-label="Blue lace border"></div>
    </div>
  </section>

</main>
</body>
</html>
```